Dunwoody Business Card Design

Small Company
looking to ramp up work need business cards sick of everyone asking for a card
client base is broad.
keep it simple
Just want on the reverse of the card somewhere for me to write details for clients
appointments etc..
want to use the phrase
"Your safe, reliable and trust worthy Tradesmen"

Industry/Entity Type

Business

Contact Information for Business Card

Dunwoody Electrical Solutions Pty Ltd
Director Bradley Dunwoody
email - dunwoodyelectricalsolutions@voltmail.example
Ph - 03 95551827
Mobile - 0491570386
Domestic, Industrial, Commercial & Mining
Electrical, Solar, Communications & Fibre
REC: 58104

```html
<!DOCTYPE html>
<html lang="en">
<head>
<meta charset="utf-8">
<title>Dunwoody Electrical Solutions – Business Card</title>
<link rel="stylesheet" href="https://fonts.googleapis.com/css2?family=Questrial&display=swap">
<style>
  :root {
    --backdrop: #e9e7e3;
    --card: #f7f6f3;
    --brand-blue: #1c3f94;
    --brand-red: #e8303f;
    --soft-blue: #a9b1d4;
    --soft-pink: #f0aeb4;
    --white: #ffffff;
    --shadow: rgba(0, 0, 0, 0.14);
  }
  * { box-sizing: border-box; margin: 0; padding: 0; }
  html, body {
    width: 1200px;
    height: 873px;
    overflow: hidden;
    background: var(--backdrop);
    font-family: "Questrial", "Helvetica Neue", Arial, sans-serif;
  }
  .stage {
    position: relative;
    width: 1200px;
    height: 873px;
  }
  .card {
    position: absolute;
    top: 266px;
    width: 540px;
    height: 340px;
    background: var(--card);
    box-shadow: 0 10px 28px var(--shadow);
    overflow: hidden;
  }

  /* Reverse side */
  .card-reverse { left: 40px; }
  .motif-area {
    position: absolute;
    left: 30px;
    top: 30px;
    width: 200px;
    height: 280px;
    border-radius: 8px;
    background: linear-gradient(135deg, var(--soft-pink) 0%, #e8c9d3 50%, var(--soft-blue) 100%);
    opacity: 0.55;
  }
  .services {
    position: absolute;
    top: 30px;
    right: 28px;
    width: 270px;
    text-align: right;
    color: var(--brand-red);
    font-size: 11.5px;
    letter-spacing: 1px;
    font-variant: small-caps;
    line-height: 2;
    white-space: nowrap;
  }
  .services .divider { color: var(--soft-blue); padding: 0 4px; }

  /* Front side */
  .card-front { left: 620px; }
  .brand {
    position: absolute;
    top: 18px;
    right: 30px;
    text-align: right;
  }
  .brand-name {
    display: flex;
    align-items: center;
    justify-content: flex-end;
    gap: 12px;
    color: var(--brand-blue);
    font-size: 44px;
    line-height: 1;
    letter-spacing: 0.5px;
  }
  .brand-dot {
    width: 14px;
    height: 14px;
    border-radius: 50%;
    background: var(--brand-red);
  }
  .brand-tagline {
    margin-top: 4px;
    color: var(--brand-red);
    font-size: 14px;
    letter-spacing: 2px;
    text-transform: uppercase;
  }
  .info-band {
    position: absolute;
    left: 0;
    right: 0;
    top: 106px;
    bottom: 26px;
    background: var(--brand-blue);
    padding: 20px 30px 0 30px;
    color: var(--white);
  }
  .holder-name {
    font-size: 22px;
    font-weight: 400;
    letter-spacing: 1.5px;
    text-transform: uppercase;
  }
  .holder-role {
    margin-top: 2px;
    font-size: 11px;
    letter-spacing: 1.5px;
    text-transform: uppercase;
  }
  .contact-list {
    list-style: none;
    margin-top: 12px;
    font-size: 12px;
    letter-spacing: 1px;
    line-height: 1.55;
  }
  .contact-list .label {
    display: inline-block;
    width: 16px;
    color: var(--brand-red);
  }
  .contact-list .email { text-transform: uppercase; }
  .motto {
    margin-top: 14px;
    color: var(--brand-red);
    font-size: 15px;
    letter-spacing: 1px;
    text-transform: uppercase;
  }
</style>
</head>
<body>
<main class="stage">

  <section class="card card-reverse" aria-label="Card reverse">
    <div class="motif-area" role="img" aria-label="Decorative field of soft pink and blue circles"></div>
    <p class="services">
      Domestic<span class="divider">|</span>Industrial<span class="divider">|</span>Commercial<span class="divider">|</span>Mining<br>
      Solar<span class="divider">|</span>Communications<span class="divider">|</span>Fibre
    </p>
  </section>

  <section class="card card-front" aria-label="Card front">
    <header class="brand">
      <div class="brand-name"><span class="brand-dot" aria-hidden="true"></span>Dunwoody</div>
      <div class="brand-tagline">Electrical Solutions</div>
    </header>
    <div class="info-band">
      <h1 class="holder-name">Bradley Dunwoody</h1>
      <p class="holder-role">Pty Ltd Director</p>
      <ul class="contact-list">
        <li><span class="label">P</span>03 95551827</li>
        <li><span class="label">M</span>0491570386</li>
        <li class="email"><span class="label">E</span>dunwoodyelectricalsolutions@voltmail.example</li>
        <li><span class="label"></span>REC 58104</li>
      </ul>
      <p class="motto">Your safe, reliable and trustworthy tradesmen</p>
    </div>
  </section>

</main>
</body>
</html>
```